Copper Heron Website

We need a website for our software / project management services company based in South Africa called "Copper Heron". We provide professional services to high value clients in the public and private sectors.

The website must present a highly professional company that exudes quality and confidence.

The theme should be a highly professional subdued look with a fairly limited palette. The neutral tone should be slightly offset with the colours from the company logo. The website should not look dead though, and subtle colour highligting should provide a fresh vibrant feel.

Refer to the current website for general content (www.copperheron.co.za) that may be used. We would also like to make use of social integration and google maps.
Updates

Thanks to all the designers that have participated so far and to those that are cooking something up at this very minute :-)

We have received a lot of designs with elements that we absolutely love. So now the hard work of refining these designs can begin.

We'll try and provide feedback on every design received so far ... and await the beautiful designs that we haven't received yet :-)

Good Luck!

Project Deadline Extended
Reason: After careful consideration we are extending the deadline to make small revisions to some of the designs and to select the top three designs. Thank you for everyone who has made a contribution so far - we have several designs that we like and selecting the best one is proving to be difficult :-)

Target Market(s)

The company deals mostly with other businesses, so mostly B2B.

Industry/Entity Type

Software

Requirements
Nice to have
• Social integration

```html
<!DOCTYPE html>
<html lang="en">
<head>
<meta charset="utf-8">
<title>Copper Heron – Software, Project Management &amp; Consulting</title>
<link href="https://fonts.googleapis.com/css2?family=Roboto+Condensed:wght@400;700&family=Roboto:wght@300;400&display=swap" rel="stylesheet">
<style>
:root{
  --bg:#e3e7dd;
  --card:#f6f6f6;
  --white:#ffffff;
  --green:#7dbb2c;
  --green-dark:#4f8d1c;
  --green-light:#a6d65a;
  --grey-band:#8a8a8a;
  --grey-dark:#5a5a5a;
  --grey-text:#a9a9a9;
  --line:#d2d2d2;
  --ink:#222;
  --orange:#f2a51c;
}
*{box-sizing:border-box;margin:0;padding:0}
html,body{width:800px;height:1200px;overflow:hidden}
body{background:radial-gradient(ellipse at 50% 40%,#f3f4ef 0%,var(--bg) 100%);font-family:"Roboto",sans-serif;position:relative}
.abs{position:absolute}
.page{left:73px;top:33px;width:662px;height:1122px;background:var(--card);box-shadow:0 0 6px rgba(0,0,0,.12)}
.cond{font-family:"Roboto Condensed",sans-serif}

/* header */
.contact-title{left:128px;top:52px;color:var(--green);font-size:18px;font-weight:700}
.phone-icon{left:84px;top:68px}
.contact-phone{left:111px;top:82px;font-size:17px;color:var(--grey-dark)}
.contact-mail{left:111px;top:111px;font-size:12px;color:var(--grey-dark)}
.main-nav{left:277px;top:67px;display:flex;gap:12px;font-size:9px;font-weight:700;color:var(--grey-dark)}
.brand-mark{left:520px;top:52px}
.brand-name{left:545px;top:78px;font-size:32px;font-weight:700;color:var(--grey-dark);letter-spacing:-.5px}
.tagline{left:474px;top:120px;font-size:12px;color:var(--grey-dark)}

/* hero */
.hero-frame{left:79px;top:147px;width:640px;height:304px;background:#fafafa;border:1px solid #ddd;border-radius:6px;box-shadow:0 3px 6px rgba(0,0,0,.15)}
.hero-photo{left:93px;top:159px;width:616px;height:249px;border-radius:6px 6px 4px 4px;background:linear-gradient(90deg,#8f8a80 0%,#c8b9a4 30%,#b28c72 55%,#3d4452 78%,#cfd3d8 100%)}
.hero-tabs{left:100px;top:400px;width:604px;height:6px;display:flex;gap:4px}
.hero-tabs span{flex:1;border-radius:3px 3px 0 0}
.hero-caption{left:83px;top:238px;width:273px;height:143px;border-radius:14px;background:linear-gradient(180deg,#6fb93a,#2f7a16);padding:14px 20px;color:#fff;font-size:22.5px;line-height:27px;box-shadow:0 2px 5px rgba(0,0,0,.3)}
.hero-dots{left:371px;top:423px;display:flex;gap:4px}
.hero-dots i{width:15px;height:15px;border-radius:50%;background:#f0f0f0;border:1px solid #d0d0d0;display:block}
.hero-dots i.on{background:#222;border:3px solid #eee}

/* services */
.services{left:74px;top:470px;width:653px;height:177px;background:#fbfbfb}
.service-head{top:8px;height:33px;background:var(--grey-band);color:#fff;font-size:16px;letter-spacing:-.2px;font-weight:700;padding:7px 5px;border-bottom:2px solid var(--green-light);white-space:nowrap;overflow:visible}
.service-body{top:59px;font-size:12.5px;line-height:15.5px;color:var(--grey-text);font-weight:300;width:200px}
.service-body p+p{margin-top:7px}
.read-more{color:var(--green);font-size:12.5px;font-weight:300}
.col-rule{top:43px;width:1px;height:132px;background:#e3e3e3}

/* process */
.process-head{left:75px;top:661px;width:341px;height:32px;background:var(--grey-band);border:2px solid #444;color:#fff;font-size:16px;font-weight:700;padding:4px 0 0 22px;white-space:nowrap}
.btn-grey{left:333px;top:897px;width:68px;height:23px;background:#8c8c8c;border-radius:3px;color:#fff;font-size:9px;font-weight:700;text-align:center;line-height:23px}

/* quote */
.quote{left:416px;top:654px;width:311px;height:266px;border:2px solid var(--green-light);background:#f9f9f9}
.quote-btn{left:431px;top:667px;width:286px;height:55px;border-radius:28px;background:linear-gradient(180deg,#a8dd5a,#6cb82a);box-shadow:0 2px 3px rgba(0,0,0,.2)}
.quote-btn .arrow{position:absolute;left:8px;top:10px;width:36px;height:36px;border-radius:50%;background:#f4f4f4}
.quote-btn .label{position:absolute;left:66px;top:15px;font-size:18px;font-weight:700;color:#1a2a10;white-space:nowrap}
.field-label{font-size:14px;color:var(--ink);font-family:"Roboto Condensed",sans-serif}
.field{background:#f1f1f1;border:1px solid #c8c8c8}
.field-note{font-size:10px;color:var(--ink);padding:8px 6px;font-family:"Roboto Condensed",sans-serif}
.submit{left:533px;top:894px;width:75px;height:21px;background:var(--green);color:#fff;font-size:12px;font-weight:700;text-align:center;line-height:21px;border-radius:2px}

/* testimonials */
.rule{height:1px;background:#cfcfcf}
.testi-title{left:192px;top:939px;font-size:19px;color:var(--grey-dark);font-weight:700}
.testi-text{left:88px;top:985px;width:310px;font-size:12.5px;line-height:15.5px;color:var(--grey-text);font-weight:300}
.testi-more{left:320px;top:1055px;color:var(--orange);font-size:12.5px;font-weight:300}
.feature-list{font-size:12px;color:var(--grey-dark);font-weight:300;white-space:nowrap}
.feature-icon{width:14px;height:14px;border-radius:3px}

/* footer */
.foot-contact{top:1091px;font-size:16px;font-weight:700;color:var(--green)}
.visit{left:484px;top:1093px;font-size:14px;font-style:italic;color:var(--green);font-family:"Roboto Condensed",sans-serif}
.social{top:1086px;width:27px;height:27px;border-radius:3px;border:1px solid #fff;box-shadow:0 0 2px rgba(0,0,0,.3)}
.foot-nav{left:93px;top:1122px;display:flex;gap:0;font-size:12px;color:var(--grey-text);font-weight:300;white-space:nowrap}
.copyright{left:80px;top:1158px;font-size:10px;color:var(--grey-text);font-family:"Roboto Condensed",sans-serif}
</style>
</head>
<body>

<div class="abs page"></div>

<header>
  <svg class="abs phone-icon" width="20" height="26" viewBox="0 0 20 26" aria-hidden="true"><path d="M4 2 Q0 13 9 24 L13 21 L9 15 L6 16 Q3 11 6 6 L9 7 L9 1 Z" fill="#8cc63f"/></svg>
  <div class="abs contact-title cond">CONTACT US</div>
  <div class="abs contact-phone cond">+27 12 555 0190</div>
  <div class="abs contact-mail">hello@copperheron.co.za</div>
  <nav class="abs main-nav cond"><span>Home</span><span>Company</span><span>Services</span><span>Portfolio</span><span>Contact</span></nav>
  <svg class="abs brand-mark" width="20" height="20" aria-hidden="true"><rect x="2" y="2" width="16" height="16" fill="#7dbb2c"/></svg>
  <div class="abs brand-name cond">Copper Heron</div>
  <div class="abs tagline cond">Premium Provider for your Software Needs</div>
</header>

<section>
  <div class="abs hero-frame"></div>
  <div class="abs hero-photo" role="img" aria-label="Smiling business consultant in a suit with colleagues in the background"></div>
  <div class="abs hero-tabs"><span style="background:#4c4668"></span><span style="background:#1f9a6a"></span><span style="background:#f06d21"></span></div>
  <div class="abs hero-caption cond">The Leader in Software Development, Project Management and Professional Consulting</div>
  <div class="abs hero-dots"><i class="on"></i><i></i><i></i></div>
</section>

<section class="abs services">
  <div class="abs service-head cond" style="left:2px;width:220px">SOFTWARE DEVELOPMENT</div>
  <div class="abs service-head cond" style="left:222px;width:220px;padding-left:8px">PROJECT MANAGEMENT</div>
  <div class="abs service-head cond" style="left:442px;width:211px;padding-left:6px">PROFESSIONAL CONSULTING</div>
  <div class="abs col-rule" style="left:214px"></div>
  <div class="abs col-rule" style="left:434px"></div>

  <div class="abs service-body" style="left:6px"><p>Cras euismod, sapien ut accum-san feugiat, mauris erat auctor metus, sed pellentesque mas.</p><p>Nullam at massa orci. Nulla suscipit adipiscing .</p></div>
  <div class="abs read-more" style="left:119px;top:161px">Read more &gt;</div>
  <div class="abs service-body" style="left:226px"><p>Cras euismod, sapien ut accum-san feugiat, mauris erat auctor metus, sed pellentesque mas.</p><p>Nullam at massa orci. Nulla suscipit adipiscing .</p></div>
  <div class="abs read-more" style="left:339px;top:161px">Read more &gt;</div>
  <div class="abs service-body" style="left:446px;top:55px"><p>Cras euismod, sapien ut accum-san feugiat, mauris erat auctor metus, sed pellentesque mas.</p><p>Nullam at massa orci. Nulla suscipit adipiscing .</p></div>
  <div class="abs read-more" style="left:559px;top:157px">Read more &gt;</div>
</section>

<section>
  <div class="abs process-head cond">OUR SOFTWARE DEVELOPMENT PROCESS</div>
  <svg class="abs" style="left:122px;top:690px" width="240" height="230" viewBox="0 0 240 230" font-family="Roboto Condensed, sans-serif" fill="#fff" text-anchor="middle">
    <defs><radialGradient id="ball" cx="40%" cy="35%" r="65%"><stop offset="0" stop-color="#a7d65c"/><stop offset="1" stop-color="#4f9a1c"/></radialGradient></defs>
    <circle cx="120" cy="118" r="82" fill="none" stroke="#cfd7c7" stroke-width="6"/>
    <circle cx="120" cy="118" r="36" fill="url(#ball)" stroke="#eef3e6" stroke-width="2"/>
    <text x="120" y="112" font-size="8.5">Software</text><text x="120" y="122" font-size="8.5">Development</text><text x="120" y="132" font-size="8.5">Lifecycle</text>
    <circle cx="120" cy="36" r="27" fill="url(#ball)" stroke="#eef3e6" stroke-width="2"/>
    <text x="120" y="35" font-size="5.5">Project</text><text x="120" y="42" font-size="5.5">Management</text>
    <circle cx="202" cy="95" r="27" fill="url(#ball)" stroke="#eef3e6" stroke-width="2"/>
    <text x="202" y="94" font-size="5.5">Software</text><text x="202" y="101" font-size="5.5">Development</text>
    <circle cx="171" cy="193" r="27" fill="url(#ball)" stroke="#eef3e6" stroke-width="2"/>
    <text x="171" y="192" font-size="5.5">Professional</text><text x="171" y="199" font-size="5.5">Consulting</text>
    <circle cx="70" cy="196" r="27" fill="url(#ball)" stroke="#eef3e6" stroke-width="2"/>
    <text x="70" y="195" font-size="5.5">Software</text><text x="70" y="202" font-size="5.5">support</text>
    <circle cx="39" cy="98" r="27" fill="url(#ball)" stroke="#eef3e6" stroke-width="2"/>
    <text x="39" y="93" font-size="5.5">Software</text><text x="39" y="100" font-size="5.5">Quality</text><text x="39" y="107" font-size="5.5">Assurance</text>
  </svg>
  <div class="abs btn-grey cond">READ MORE</div>
</section>

<section>
  <div class="abs quote"></div>
  <div class="abs quote-btn">
    <span class="arrow"><svg width="36" height="36" aria-hidden="true"><path d="M15 11 L22 18 L15 25" fill="none" stroke="#7dbb2c" stroke-width="3"/></svg></span>
    <span class="label cond">REQUEST A FREE QUOTE</span>
  </div>
  <div class="abs field-label" style="left:428px;top:735px">NAME:</div>
  <div class="abs field" style="left:507px;top:730px;width:212px;height:31px"></div>
  <div class="abs field-label" style="left:428px;top:782px">EMAIL:</div>
  <div class="abs field" style="left:507px;top:775px;width:212px;height:31px"></div>
  <div class="abs field field-note" style="left:423px;top:814px;width:296px;height:68px">QUESTIONS OR COMMENTS:</div>
  <div class="abs submit cond">SUBMIT</div>
</section>

<section>
  <div class="abs rule" style="left:75px;top:927px;width:652px"></div>
  <svg class="abs" style="left:83px;top:941px" width="45" height="36" aria-hidden="true"><ellipse cx="15" cy="12" rx="14" ry="10" fill="#f5c518"/><ellipse cx="30" cy="20" rx="13" ry="11" fill="#7dbb2c"/><path d="M28 29 L26 35 L33 30 Z" fill="#7dbb2c"/></svg>
  <div class="abs testi-title cond">TESTIMONIALS</div>
  <div class="abs testi-text"><p>Cras euismod, sapien ut accumsan feugiat, mauris erat auctor metus, sed pellentesque mas.</p><p style="margin-top:7px">Nullam at massa orci. Nulla suscipit adipiscing .</p></div>
  <div class="abs testi-more">read more &gt;</div>
  <div class="abs" style="left:409px;top:941px;width:1px;height:138px;background:#d6d6d6"></div>

  <div class="feature-list">
    <span class="abs feature-icon" style="left:442px;top:953px;background:#c9a26a"></span><span class="abs" style="left:489px;top:951px">Custom Software</span>
    <span class="abs feature-icon" style="left:442px;top:988px;background:#333"></span><span class="abs" style="left:489px;top:990px">Custom Software</span>
    <span class="abs feature-icon" style="left:442px;top:1024px;background:#4a7fb5"></span><span class="abs" style="left:489px;top:1021px">Custom Software</span>
    <span class="abs feature-icon" style="left:442px;top:1057px;background:#9a9a9a;border-radius:50%"></span><span class="abs" style="left:489px;top:1052px">Custom Software</span>
    <span class="abs feature-icon" style="left:590px;top:957px;background:#444"></span><span class="abs" style="left:625px;top:956px">Custom Software</span>
    <span class="abs feature-icon" style="left:590px;top:991px;background:#5b84d8"></span><span class="abs" style="left:625px;top:987px">Custom Software</span>
    <span class="abs feature-icon" style="left:590px;top:1022px;background:#6d8fb0"></span><span class="abs" style="left:625px;top:1019px">Custom Software</span>
    <span class="abs feature-icon" style="left:590px;top:1057px;background:#8fb0d8"></span><span class="abs" style="left:625px;top:1050px">Custom Software</span>
  </div>
</section>

<footer>
  <div class="abs rule" style="left:88px;top:1083px;width:632px"></div>
  <div class="abs foot-contact cond" style="left:99px">+27 12 555 0190</div>
  <div class="abs foot-contact cond" style="left:259px">hello@copperheron.co.za</div>
  <div class="abs visit">Visit Us:</div>
  <span class="abs social" style="left:562px;background:#f06d21" role="img" aria-label="Blog"></span>
  <span class="abs social" style="left:607px;background:#3b5a9a" role="img" aria-label="Social profile"></span>
  <span class="abs social" style="left:653px;background:#1d7fb3" role="img" aria-label="Professional network"></span>
  <span class="abs social" style="left:698px;background:#32b8e8" role="img" aria-label="Microblog"></span>
  <nav class="abs foot-nav">
    <span style="width:86px">HOME</span><span style="width:90px">COMPANY</span><span style="width:175px">PROFESSIONAL SERVICES</span><span style="width:86px">PORTFOLIO</span><span style="width:105px">CONTACT US</span><span>SITE MAP</span>
  </nav>
  <div class="abs copyright">Copyright 2009 Copper Heron.&nbsp; All Rights Reserved.&nbsp; Legal</div>
</footer>

</body>
</html>
```